Ridecraft Academy Wordpress Motorcycle School Business Website

We are a motorcycle training school that is located in Calgary, AB, Canada. Our main service is motorcycle safety training. We currently have a site at www.ridecraftacademy.example . We would like to see a design whereby the colours align with our logo (a white background is best), as well as effectively communicating our strengths as a school and the value and quality of the services we provide.

There are also photos on our facebook page at: www.facebook.com/ridecraftacademy/ , it would be nice to incorporate some, but we are open to using generic photos as well.

It is important that the entire site be mobile friendly. The front page should be able to house all the information that a potential student would be looking for in terms of WHY they should choose us, without having to navigate to secondary pages.

We also currently have a small youtube clip that we would like to keep on the main page to "hook" a potential customer. We have secondary pages in our menu for further details and also have an integrated booking engine on one of the pages so that student's can book and pay online. These things we would like to keep. It would also be nice to give the ability for our customers to share the website's pages on social media.

Our current subpages are:
About Us
Our Staff
Our Fleet
Client Testimonials
Friends of Ridecraft
Course Descriptions
Course Pricing
Bookings (where they book)
FAQ
Privacy Policy
Contact Page

A more efficient and effective method of organizing/delivering the content would be great.

Finally... a sleek, modern/contemporary theme is what we are after. Our company slogan being: Fun - Safe - Professional

Please reference the existing website for all the necessary content.

Target Market(s)

18-50 year old. Motorcycle enthusiast students who want to learn to ride.

Industry/Entity Type

Driving School

Font styles to use
Sans Serif

Requirements
Must have
• Some photos from our facebook page would be great.
• Ridecraft Academy Logo colours
• Please refer to the Project Description.
Nice to have
• Modern/Contemporary

```html
<!DOCTYPE html>
<html lang="en">
<head>
<meta charset="utf-8">
<title>Ridecraft Academy</title>
<link href="https://fonts.googleapis.com/css2?family=Open+Sans:wght@400;600;700;800&display=swap" rel="stylesheet">
<style>
:root{
  --yellow:#f7c21a;
  --yellow-dark:#e5ad00;
  --ink:#222222;
  --text:#555555;
  --muted:#8a8a8a;
  --line:#dddddd;
  --panel:#f1f1f1;
  --white:#ffffff;
  --footer:#1e1e1e;
  --footer-text:#a8a8a8;
}
*{box-sizing:border-box;margin:0;padding:0}
html,body{width:1200px;height:2808px;overflow:hidden}
body{font-family:"Open Sans",Arial,sans-serif;color:var(--text);background:var(--white);position:relative}
.abs{position:absolute}

/* header */
.site-header{position:absolute;left:0;top:0;width:1200px;height:140px;background:var(--white)}
.brand{left:100px;top:38px;display:flex;align-items:center;gap:14px}
.brand-dot{width:44px;height:44px;border-radius:50%;background:var(--yellow)}
.brand-name{font-size:38px;font-weight:800;color:var(--ink);letter-spacing:-0.5px}
.search{left:708px;top:48px;width:150px;height:40px;border:1px solid var(--line);display:flex;align-items:center;padding-left:12px;gap:8px;font-size:15px;color:var(--muted)}
.call{left:912px;top:40px;display:flex;gap:12px;align-items:center}
.call-icon{width:48px;height:48px;border-radius:50%;background:var(--yellow);display:flex;align-items:center;justify-content:center}
.call-label{font-size:13px;font-weight:700;color:var(--muted);letter-spacing:1px}
.call-number{font-size:24px;font-weight:800;color:var(--ink)}

.main-nav{position:absolute;left:0;top:140px;width:1200px;height:52px;background:var(--ink);display:flex;padding-left:92px}
.main-nav a{color:var(--white);font-size:15px;font-weight:600;text-decoration:none;padding:0 19px;line-height:52px}
.main-nav a.active{background:var(--yellow)}

/* hero */
.hero{position:absolute;left:0;top:192px;width:1200px;height:576px;background:linear-gradient(180deg,#c9d7e6 0%,#aebccb 45%,#8d9196 70%,#6e6f72 100%)}
.hero-slogan{left:0;top:320px;width:1200px;text-align:center;font-size:44px;font-weight:800;color:var(--white);letter-spacing:2px;text-shadow:0 2px 6px rgba(0,0,0,.4)}
.btn{display:inline-block;background:var(--yellow);color:var(--white);font-weight:700;font-size:17px;letter-spacing:1px;text-transform:uppercase;text-align:center}
.hero-btn{left:490px;top:408px;width:220px;height:56px;line-height:56px}
.dots{left:0;top:520px;width:1200px;display:flex;justify-content:center;gap:10px}
.dots span{width:14px;height:14px;border-radius:50%;background:var(--white);opacity:.8}
.dots span.on{background:transparent;border:2px solid var(--white);opacity:1}

/* courses */
.courses{position:absolute;left:0;top:768px;width:1200px;height:412px;background:var(--white)}
.course-card{top:52px;width:488px;height:318px;border:1px solid var(--line);background:var(--white);display:flex}
.course-text{width:262px;padding:28px 22px 28px 24px}
.course-title{font-size:21px;font-weight:700;color:var(--yellow);line-height:1.25;white-space:nowrap}
.course-title b{color:var(--ink);font-weight:700;display:block}
.course-text p{font-size:15px;line-height:1.6;margin-top:18px;color:var(--muted)}
.btn-dark{display:inline-block;background:var(--ink);color:var(--white);font-size:14px;font-weight:700;padding:0 18px;height:40px;line-height:40px;margin-top:28px}
.course-photo{flex:1;margin:14px 14px 14px 0;background:linear-gradient(160deg,#d9e5f0 0%,#a9b4bd 55%,#5d6167 100%)}

/* why band */
.why{position:absolute;left:0;top:1180px;width:1200px;height:520px;background:var(--yellow)}
.why-card{left:100px;top:80px;width:452px;height:360px;background:var(--white);padding:24px}
.why-title{font-size:20px;font-weight:800;color:var(--yellow);text-transform:uppercase}
.why-sub{font-size:15px;color:var(--ink);margin-top:2px}
.why-photo{margin-top:16px;height:172px;background:linear-gradient(170deg,#c7d5b4 0%,#7f9a63 60%,#55693f 100%)}
.video{left:576px;top:80px;width:524px;height:360px;background:var(--white);padding:14px}
.video-frame{width:100%;height:100%;background:radial-gradient(circle at 50% 50%,#ffffff 0%,#eef0f2 55%,#c6ccd2 100%);position:relative}
.play{left:216px;top:134px;width:64px;height:64px;border-radius:50%;background:var(--ink);opacity:.85;display:flex;align-items:center;justify-content:center;padding-left:5px}

/* news + booking */
.news{left:100px;top:1712px;width:600px}
.section-title{font-size:24px;font-weight:800;color:var(--yellow);text-transform:uppercase}
.news-arrows{left:524px;top:0;display:flex;gap:8px}
.news-arrows span{width:36px;height:36px;border-radius:50%;background:#bbbbbb;display:flex;align-items:center;justify-content:center}
.news-list{margin-top:30px;background:var(--panel);padding:24px;height:370px}
.news-item{background:var(--white);padding:16px 20px 16px 40px;margin-bottom:16px;font-size:14px;line-height:1.55;color:var(--muted);position:relative}
.news-item::before{content:"";position:absolute;left:18px;top:22px;width:8px;height:8px;border-top:2px solid var(--muted);border-right:2px solid var(--muted);transform:rotate(45deg)}
.news-item .more{color:var(--yellow);font-weight:600}

.booking{left:732px;top:1712px;width:368px}
.booking-form{margin-top:30px}
.field{height:48px;border:1px solid var(--line);margin-bottom:12px;padding-left:16px;font-size:15px;color:var(--muted);line-height:46px;position:relative}
.field .icon{position:absolute;right:14px;top:0}
.book-btn{width:100%;height:60px;line-height:60px;font-size:22px}

/* call to action */
.cta{left:100px;top:2196px;width:1000px;height:196px;border:3px solid var(--line);text-align:center;padding-top:36px}
.cta h2{font-size:22px;font-weight:800;color:var(--yellow);text-transform:uppercase}
.cta p{font-size:16px;margin-top:8px}
.cta .btn{margin-top:26px;height:52px;line-height:52px;padding:0 32px;font-size:16px}

/* footer */
.site-footer{position:absolute;left:0;top:2448px;width:1200px;height:360px;background:var(--footer);color:var(--footer-text)}
.foot-col h3{font-size:16px;font-weight:700;color:var(--white);text-transform:uppercase}
.foot-contact{left:100px;top:38px;font-size:14px;line-height:1.75}
.foot-contact p{margin-top:16px}
.foot-follow{left:472px;top:38px}
.socials{display:flex;gap:14px;margin-top:22px}
.socials span{width:26px;height:26px;border-radius:50%;background:#555555}
.foot-news{left:756px;top:38px}
.foot-news h3{text-transform:none;font-weight:600}
.subscribe{margin-top:22px;width:344px;height:52px;background:#2e2e2e;display:flex;align-items:center;padding-left:16px;gap:12px;font-size:14px;position:relative}
.subscribe .go{position:absolute;right:14px;top:14px}
.foot-rule{left:100px;top:240px;width:1000px;height:1px;background:#3a3a3a}
.foot-links{left:100px;top:262px;width:600px;font-size:13px;line-height:2;color:var(--footer-text)}
.foot-links span{margin-right:20px}
.copyright{left:820px;top:270px;width:280px;font-size:13px;text-align:right}
</style>
</head>
<body>

<header class="site-header">
  <div class="abs brand"><span class="brand-dot"></span><span class="brand-name">Ridecraft Academy</span></div>
  <div class="abs search">
    <svg width="16" height="16" viewBox="0 0 16 16"><circle cx="7" cy="7" r="5" fill="none" stroke="#8a8a8a" stroke-width="2"/><line x1="11" y1="11" x2="15" y2="15" stroke="#8a8a8a" stroke-width="2"/></svg>
    Search
  </div>
  <div class="abs call">
    <div class="call-icon"><svg width="22" height="22" viewBox="0 0 24 24"><path d="M6.6 10.8a15.2 15.2 0 0 0 6.6 6.6l2.2-2.2a1 1 0 0 1 1-.25 11.4 11.4 0 0 0 3.6.57 1 1 0 0 1 1 1V20a1 1 0 0 1-1 1A17 17 0 0 1 3 4a1 1 0 0 1 1-1h3.5a1 1 0 0 1 1 1c0 1.25.2 2.450.57 3.57a1 1 0 0 1-.25 1z" fill="#fff"/></svg></div>
    <div><div class="call-label">CALL BOOK NOW</div><div class="call-number">403.555.0142</div></div>
  </div>
</header>

<nav class="main-nav">
  <a class="active">Home</a><a>About Us</a><a>Our Staff</a><a>Our Fleet</a><a>Testimonials</a><a>Friends of Ridecraft</a><a>Course Pricing</a><a>Bookings</a><a>Contact Us</a>
</nav>

<section class="hero" role="img" aria-label="Photo of a row of sport motorcycles parked on a training lot">
  <div class="abs hero-slogan">FUN - SAFE - PROFESSIONAL</div>
  <div class="abs btn hero-btn">Learn More &rsaquo;</div>
  <div class="abs dots"><span></span><span class="on"></span><span></span><span></span><span></span></div>
</section>

<section class="courses">
  <div class="abs course-card" style="left:100px">
    <div class="course-text">
      <div class="course-title">Basic Motorcycle<b>Training</b></div>
      <p>Ridecraft Academy teaches you to become a rider who is knowledgeable, responsible.</p>
      <span class="btn-dark">BOOK NOW</span>
    </div>
    <div class="course-photo" role="img" aria-label="Photo of a student rider on a motorcycle in a parking lot"></div>
  </div>
  <div class="abs course-card" style="left:612px">
    <div class="course-text">
      <div class="course-title">Rider Proficiency<b>Training</b></div>
      <p>Ridecraft Academy teaches you to become a rider who is knowledgeable, responsible.</p>
      <span class="btn-dark">BOOK NOW</span>
    </div>
    <div class="course-photo" role="img" aria-label="Photo of a rider on a red motorcycle during a training exercise"></div>
  </div>
</section>

<section class="why">
  <div class="abs why-card">
    <div class="why-title">Why choose us?</div>
    <div class="why-sub">What makes us different from others?</div>
    <div class="why-photo" role="img" aria-label="Photo of an instructor standing beside a motorcycle"></div>
    <span class="btn-dark">READ MORE</span>
  </div>
  <div class="abs video">
    <div class="video-frame" role="img" aria-label="Video thumbnail showing a classic motorcycle">
      <div class="abs play"><svg width="22" height="26" viewBox="0 0 22 26"><path d="M2 2l18 11L2 24z" fill="#fff"/></svg></div>
    </div>
  </div>
</section>

<section class="abs news">
  <div class="section-title">News</div>
  <div class="abs news-arrows">
    <span><svg width="12" height="14" viewBox="0 0 12 14"><path d="M9 1L3 7l6 6" fill="none" stroke="#fff" stroke-width="2.5"/></svg></span>
    <span><svg width="12" height="14" viewBox="0 0 12 14"><path d="M3 1l6 6-6 6" fill="none" stroke="#fff" stroke-width="2.5"/></svg></span>
  </div>
  <div class="news-list">
    <div class="news-item">Our 2017 season is coming to an end in September. Book your course now if you still want to get it before the end of the year.<br><span class="more">READ MORE</span></div>
    <div class="news-item">Check out our Friends of Ridecraft page for our relationships and deals for our students. More added twice and the support...<br><span class="more">READ MORE</span></div>
    <div class="news-item">Rider tip: plan your braking early, keep your eyes up and look well ahead through every turn you make on the road...<br><span class="more">READ MORE</span></div>
  </div>
</section>

<section class="abs booking">
  <div class="section-title">Quick Book</div>
  <div class="booking-form">
    <div class="field">Name</div>
    <div class="field">E-mail</div>
    <div class="field">Select Course<svg class="icon" width="12" height="46" viewBox="0 0 12 46"><path d="M1 20l5 5 5-5" fill="none" stroke="#8a8a8a" stroke-width="2"/></svg></div>
    <div class="field">DD/MM/YYYY<svg class="icon" width="16" height="46" viewBox="0 0 16 46"><rect x="1" y="16" width="14" height="13" fill="none" stroke="#8a8a8a" stroke-width="1.6"/><line x1="1" y1="20" x2="15" y2="20" stroke="#8a8a8a" stroke-width="1.6"/></svg></div>
    <div class="field">Subject</div>
    <div class="btn book-btn">BOOK NOW</div>
  </div>
</section>

<section class="abs cta">
  <h2>We are Ridecraft Academy, have questions about our classes?</h2>
  <p>Call Us at 403.555.0142 or info@ridecraftacademy.example</p>
  <span class="btn">Get in touch with us</span>
</section>

<footer class="site-footer">
  <div class="abs foot-col foot-contact">
    <h3>Contact Us</h3>
    <p>120 Riverbend Way, Calgary,<br>AB T2X 0A1 | 403.555.0142<br>E: info@ridecraftacademy.example</p>
  </div>
  <div class="abs foot-col foot-follow">
    <h3>Follow Us On</h3>
    <div class="socials"><span></span><span></span><span></span><span></span></div>
  </div>
  <div class="abs foot-col foot-news">
    <h3>Subscribe to our newsletter for Ridecraft News!</h3>
    <div class="subscribe">
      <svg width="18" height="14" viewBox="0 0 18 14"><rect x="1" y="1" width="16" height="12" fill="none" stroke="#a8a8a8" stroke-width="1.6"/><path d="M1 1l8 6 8-6" fill="none" stroke="#a8a8a8" stroke-width="1.6"/></svg>
      E-mail Address
      <svg class="go" width="14" height="24" viewBox="0 0 14 24"><path d="M3 4l8 8-8 8" fill="none" stroke="#f7c21a" stroke-width="3"/></svg>
    </div>
  </div>
  <div class="abs foot-rule"></div>
  <div class="abs foot-links">
    <span>Home</span><span>About Us</span><span>Our Staff</span><span>Our Fleet</span><span>Client Testimonials</span><span>Friends of Ridecraft</span><br>
    <span>Course Descriptions</span><span>Course Pricing</span><span>Bookings</span><span>Privacy Policy</span><span>Contact Us</span>
  </div>
  <div class="abs copyright">Copyright &copy; 2017 All Rights Reserved</div>
</footer>

</body>
</html>
```